Zielgruppe
Herstellung und Vertrieb von Baustoffen als Eigenmarke
Aufgabenstellung
Wiedererkennungswert unserer Marke. Technisches Verständniss für die Umsetrzung. Klares Design. Logo muss mit eingebaut werden. Rundes etikett mit Durchmesser 18 cm.

```html
<!DOCTYPE html>
<html lang="de">
<head>
<meta charset="utf-8">
<title>Bitumen Alu Dichtband – Etikett</title>
<link rel="stylesheet" href="https://fonts.googleapis.com/css2?family=Lato:wght@300;400;700&family=Montserrat:wght@700&family=Quicksand:wght@500;700&display=swap">
<style>
  :root {
    --paper: #ffffff;
    --ring: #7a3a28;
    --label-black: #000000;
    --accent-orange: #e4501e;
    --tape-grey: #bdb9b5;
    --tape-brown: #6b3324;
    --ink-dark: #1d1d1d;
    --ink-light: #ffffff;
  }
  html, body {
    margin: 0;
    padding: 0;
    width: 1200px;
    height: 1200px;
    overflow: hidden;
    background: var(--paper);
  }
  .label {
    position: relative;
    width: 1200px;
    height: 1200px;
    font-family: "Lato", sans-serif;
    color: var(--ink-light);
  }
  .label__shapes {
    position: absolute;
    inset: 0;
  }
  .intro {
    position: absolute;
    left: 295px;
    top: 163px;
    width: 620px;
    margin: 0;
    font-size: 15.2px;
    line-height: 21.4px;
    text-align: center;
  }
  .intro__line { display: block; white-space: nowrap; }
  .intro__line--justified {
    text-align: justify;
    text-align-last: justify;
    white-space: normal;
  }
  .intro__line--narrow { margin: 0 34px; }
  .title {
    position: absolute;
    left: 0;
    width: 1210px;
    margin: 0;
    text-align: center;
  }
  .title--small {
    top: 310px;
    font-family: "Lato", sans-serif;
    font-weight: 300;
    font-size: 94px;
    letter-spacing: 1px;
    line-height: 110px;
    color: var(--ink-light);
  }
  .title--large {
    top: 412px;
    font-family: "Montserrat", sans-serif;
    font-weight: 700;
    font-size: 100px;
    line-height: 120px;
    letter-spacing: -1px;
    color: var(--accent-orange);
  }
  .tape-text {
    position: absolute;
    margin: 0;
    font-family: "Quicksand", sans-serif;
    font-weight: 500;
    text-align: justify;
  }
  .tape-text strong { font-weight: 700; }
  .tape-text--processing {
    left: 67px;
    top: 585px;
    width: 572px;
    font-size: 13.6px;
    line-height: 16.6px;
    letter-spacing: 0.45px;
    color: var(--ink-dark);
    transform: rotate(0.4deg);
    transform-origin: left top;
  }
  .tape-text--technical {
    left: 666px;
    top: 688px;
    width: 440px;
    font-size: 14px;
    line-height: 19px;
    letter-spacing: 0.35px;
    color: var(--ink-light);
  }
  .maker {
    position: absolute;
    left: 372px;
    top: 880px;
    display: flex;
    align-items: flex-start;
    gap: 30px;
  }
  .maker__square {
    width: 100px;
    height: 100px;
    margin-top: 40px;
    border: 5px solid var(--accent-orange);
    box-sizing: border-box;
  }
  .maker__details {
    font-style: normal;
    font-size: 16.8px;
    line-height: 21.2px;
    padding-top: 27px;
  }
  .maker__name {
    display: block;
    font-weight: 700;
    font-size: 16px;
    margin-left: 3px;
    margin-bottom: 1px;
  }
  .maker__line { display: block; }
</style>
</head>
<body>
<div class="label">
  <svg class="label__shapes" width="1200" height="1200" viewBox="0 0 1200 1200" aria-hidden="true">
    <circle cx="604" cy="601" r="559" fill="none" stroke="var(--ring)" stroke-width="3.5"/>
    <circle cx="605" cy="603" r="500" fill="var(--label-black)"/>
    <line x1="169" y1="364" x2="386" y2="364" stroke="var(--ink-light)" stroke-width="4"/>
    <line x1="822" y1="364" x2="1045" y2="364" stroke="var(--ink-light)" stroke-width="4"/>
    <polygon points="652,677 1146,678 1144,720 1140,770 1120,830 1100,856 590,860 586,830 560,790 650,788" fill="var(--tape-brown)"/>
    <polygon points="44,573 666,571 660,580 672,592 662,606 674,640 666,672 672,700 658,730 666,760 652,772 655,784 185,797 120,792 50,790 44,700 47,640" fill="var(--tape-grey)"/>
  </svg>

  <p class="intro">
    <span class="intro__line">Das Bitumen Alu Dichtband klebt und dichtet zuverläs-</span>
    <span class="intro__line">sig Metall, Kunststoffe, monolithische Untergründe, Holz und Glas.</span>
    <span class="intro__line intro__line--justified intro__line--narrow">Es ist besonders geeignet zum Abdichten von: Fugen und Rissen,</span>
    <span class="intro__line intro__line--justified">Regenrinnen, Anschlüssen an Dach und Wand, Abdeckungen, Glasdächern und</span>
    <span class="intro__line">Gewächshäusern, Stahlkonstruktionen, Dacheindeckungen, Trauf- und Kehlblechen</span>
  </p>

  <h1 class="title title--small">BITUMEN</h1>
  <h2 class="title title--large">ALU DICHTBAND</h2>

  <p class="tape-text tape-text--processing"><strong>Verarbeitung:</strong>&nbsp;&nbsp; Die zu dichtenden Oberflächen müssen trocken, frost-, fett- und silikonfrei sowie abriebfest sein. Poröser oder staubiger Untergrund sollte mit Voranstrich (ca. 200ml/m2) vorbehandelt werden, um eine optimale Haftung zu erzielen. Die günstigste Verarbeitungstemperatur liegt zwischen 5°C und 45°C, Luft bzw. Oberflächentemperatur. Es wird zur besseren Haftung im Niedrigtemperaturbereich empfohlen das Bitumen Alu Dichtband bei Raumtemperatur zu lagern. Das Bitumen Alu Dichtband muss nach dem Aufbringen fest angedrückt werden. Das Entstehen von Hohlstellen (Blasen) ist zu vermeiden. Sind mehrere Streifen anzusetzen muss die Überlappung mind. 50 mm betragen. Begehbare- bzw. befahrbare Untergründe sind zur Verarbeitung nicht geeignet.</p>

  <p class="tape-text tape-text--technical">Technische Angaben:&nbsp;&nbsp;&nbsp; Bitumen Alu Dichtband ist ein selbstklebendes und kalt zu verarbeitendes Abdichtungsband. Die Alufolie ist oberflächenvergütet, UV-beständig und hat daher eine gute mechanische Standfestigkeit. Die Beschichtungsmasse besteht aus einem hochwertigen Kunststoff-Harz-Bitumen-Gemisch, welches durch eine silikonbeschichtete Folie geschützt wird.</p>

  <div class="maker">
    <div class="maker__square" aria-hidden="true"></div>
    <address class="maker__details">
      <span class="maker__name">BRANDAU BAUSTOFFE GMBH &amp; CO. KG</span>
      <span class="maker__line">Am Kalkofen 7, 74900 Lindbach</span>
      <span class="maker__line">Telefon : 07123-48260</span>
      <span class="maker__line">Fax : 48261</span>
      <span class="maker__line">mail: info@brandau-baustoffe.de</span>
      <span class="maker__line">www.brandau-baustoffe.de</span>
    </address>
  </div>
</div>
</body>
</html>
```